Business Card Design Project

I would like to have a project of business card with incorporated attachted logo elements in warm colors like: gold, yellow, brown.
We would like incorporate below information into the design
Name of the Company: Continental Hoop Tournament
Name: Marlow Teague
Position: Project Director
e-mail: marlow@hooptournamentx.com
mobile: +65 93718402
website: www.hooptournamentx.com
Address: 47 Brindle Road, #08-05, Singapore 917264
There is a picture attachted which can be used as a back side of the buisness card - we would like to follow the colors theme on the front card ( with the person contact details) how ever the front card we will prefer with white background but with graphfic elements coming from logo.
Updates
Project Deadline Extended
Reason: the project has been launched on 24 of April with deadline by 24 of April by mistakes. Thats why I would like to extend the deadline.
Name: Marlow Teague
mobile: +65 93718402

```html
<!DOCTYPE html>
<html lang="en">
<head>
<meta charset="utf-8">
<title>Marlow Teague – Business Card</title>
<link rel="stylesheet" href="https://fonts.googleapis.com/css2?family=Montserrat:wght@400;600;700&family=Lato:wght@400&display=swap">
<style>
  :root {
    --stage: #d6d6d6;
    --gold-deep: #b87a1c;
    --gold-mid: #c9981a;
    --gold-bright: #d8c80a;
    --brown: #5e3a06;
    --ink: #0a0a0a;
    --white: #ffffff;
    --rule: #9a9a9a;
  }
  * { margin: 0; padding: 0; box-sizing: border-box; }
  html, body { width: 1200px; height: 900px; overflow: hidden; }
  body { background: var(--stage); position: relative; font-family: "Lato", sans-serif; }

  .card {
    position: absolute;
    border-radius: 14px;
    overflow: hidden;
    box-shadow: 0 4px 10px rgba(0,0,0,0.35);
  }
  .card svg.card-art { position: absolute; inset: 0; }

  .card-front {
    left: 104px; top: 72px; width: 614px; height: 338px;
    background:
      radial-gradient(ellipse 240px 170px at 270px 70px, #e2d21a 0%, rgba(226,210,26,0) 100%),
      linear-gradient(90deg, var(--gold-mid) 0%, var(--gold-deep) 100%);
  }
  .brand-visual {
    position: absolute; left: 124px; top: 30px; width: 200px; height: 160px;
    border-radius: 50%;
    background: radial-gradient(ellipse at 55% 45%, rgba(120,80,20,0.7), rgba(120,80,20,0.15) 70%, rgba(120,80,20,0) 100%);
  }
  .brand-name {
    position: absolute; left: 84px; top: 198px; width: 280px;
    font-family: "Montserrat", sans-serif; font-weight: 700;
    font-size: 11px; letter-spacing: 1px; text-transform: uppercase;
    color: var(--brown); text-align: center; white-space: nowrap;
  }
  .holder-name {
    position: absolute; left: 229px; top: 224px;
    font-family: "Montserrat", sans-serif; font-size: 30px; line-height: 1;
    color: var(--white); letter-spacing: -0.5px;
  }
  .holder-name .first { font-weight: 700; }
  .holder-name .last { font-weight: 400; }
  .name-rule {
    position: absolute; left: 226px; top: 262px; width: 388px; height: 1px;
    background: rgba(255,255,255,0.6);
  }
  .holder-role {
    position: absolute; left: 231px; top: 265px;
    font-size: 12px; color: var(--white);
  }

  .card-back {
    left: 484px; top: 482px; width: 616px; height: 338px;
    background: var(--ink);
  }
  .contact-list { position: absolute; inset: 0; }
  .contact-row {
    position: absolute; right: 250px;
    color: var(--white); white-space: nowrap; text-align: right;
  }
  .contact-row.phone { top: 186px; font-size: 13px; }
  .contact-row.email { top: 207px; font-size: 11px; }
  .contact-row.web { top: 226px; font-size: 11px; }
  .contact-row.address { top: 246px; font-size: 11px; }
</style>
</head>
<body>

<section class="card card-front" aria-label="Business card front">
  <svg class="card-art" width="614" height="338" viewBox="0 0 614 338">
    <defs>
      <linearGradient id="frontWave" x1="0" y1="0" x2="1" y2="0">
        <stop offset="0" stop-color="#c9a814"/>
        <stop offset="1" stop-color="#e0c800"/>
      </linearGradient>
      <linearGradient id="frontBand" x1="0" y1="0" x2="1" y2="0">
        <stop offset="0" stop-color="#9a6512"/>
        <stop offset="1" stop-color="#b08018"/>
      </linearGradient>
    </defs>
    <path d="M0 166 C60 220 130 285 230 298 C330 310 430 288 520 300 C565 306 595 320 614 338 L0 338 Z" fill="url(#frontBand)"/>
    <path d="M0 182 C60 240 140 300 240 306 C330 311 420 292 510 306 C555 313 590 326 605 338 L0 338 Z" fill="url(#frontWave)"/>
  </svg>
  <div class="brand-visual" role="img" aria-label="Brand artwork: performer on a hoop over the tournament emblem"></div>
  <div class="brand-name">Continental Hoop Tournament</div>
  <div class="holder-name"><span class="first">Marlow</span><span class="last">Teague</span></div>
  <div class="name-rule"></div>
  <div class="holder-role">Project Director</div>
</section>

<section class="card card-back" aria-label="Business card back">
  <svg class="card-art" width="616" height="338" viewBox="0 0 616 338">
    <defs>
      <linearGradient id="backWave" x1="0" y1="0" x2="1" y2="0">
        <stop offset="0" stop-color="#e0d000"/>
        <stop offset="1" stop-color="#b8860e"/>
      </linearGradient>
    </defs>
    <path d="M0 338 L0 330 C80 290 200 282 300 286 C420 292 540 250 616 140 L616 338 Z" fill="#8a5a10"/>
    <path d="M0 338 C90 300 200 296 300 298 C420 300 550 262 616 170 L616 338 Z" fill="url(#backWave)"/>
    <g class="rules" stroke="#8a8a8a" stroke-width="1">
      <line x1="370" y1="88" x2="370" y2="283"/>
      <line x1="0" y1="263" x2="404" y2="263"/>
      <line x1="188" y1="205" x2="404" y2="205"/>
      <line x1="188" y1="224" x2="404" y2="224"/>
      <line x1="188" y1="243" x2="404" y2="243"/>
    </g>
    <g class="icons" fill="#ffffff">
      <circle cx="380" cy="196" r="5.5"/>
      <circle cx="380" cy="215" r="5.5"/>
      <circle cx="380" cy="234" r="5.5"/>
      <circle cx="380" cy="254" r="5.5"/>
    </g>
    <g class="icon-marks" fill="#0a0a0a" stroke="#0a0a0a">
      <path d="M377.5 193.5 l1.5 0 l0.8 1.8 l-0.9 0.7 a4 4 0 0 0 1.8 1.8 l0.7 -0.9 l1.8 0.8 l0 1.5 a5 5 0 0 1 -5.7 -5.7z" stroke="none"/>
      <rect x="377" y="213" width="6" height="4" fill="none" stroke-width="0.9"/>
      <circle cx="380" cy="234" r="3" fill="none" stroke-width="0.9"/>
      <path d="M380 258 C378 255 377.5 254 377.5 252.8 a2.5 2.5 0 0 1 5 0 c0 1.2 -0.5 2.2 -2.5 5.2z" stroke="none"/>
      <circle cx="380" cy="252.8" r="0.9" fill="#ffffff" stroke="none"/>
    </g>
  </svg>
  <div class="contact-list">
    <div class="contact-row phone">+65 93718402</div>
    <div class="contact-row email">marlow@hooptournamentx.com</div>
    <div class="contact-row web">www.hooptournamentx.com</div>
    <div class="contact-row address">47 Brindle Road, #08-05, Singapore 917264</div>
  </div>
</section>

</body>
</html>
```